Brickline Gains Online Redesign

The company needs a new online presence built that better represents who we are and what we do. Our online presence needs to be optimised for both PC, tablet and Phone usage.

Our existing site; www.bricklinegains.com.au - this page currently forwards to one of our sales pages.
The entire site needs to be redesigned along with the sales pages /workshop and /faststart

Here are our competition:
https://www.coraltemsby.com/
http://quorvahomeschooling.com.au/property-education-experts/coral-temsby/
http://harrietvolonsky.com.au/
www.refitforyield.com.au/
http://fullmanualtorefurb.com.au/

Target Market(s)

40-55 Husband and Wife with children that are busy profesionals with a family income of 150-300k PA with 2-3 kids

Industry/Entity Type

Education

Number of Pages Required

5+ page

Font styles to use
Sans Serif
Script

Colors

Designer to choose colors to be used in the design.

Requirements
Must have
• Main Page
• Events Page
• Media Page
• Past Projects
• Blog - plesae design a template blog; both individual blogs and library (i like this http://bram.blog/)
• eBooks page
• Shopping Cart - buy eBooks, eBook Packs and courses
• eBook download page for each eBook
• Testimonials
• Event Sales Page
• 2 hr Event - currently www.bricklinegains.com.au/workshop & /faststart & /faststartv
Nice to have
• A few different options for sales landing pages to sell the 2 hr event
• A few different blog templates - video, text, infographic etc
• The business is a Property Educatiom, Mentoring and Consulting Company
Should not have
• This is not a real estate sales business

```html
<!DOCTYPE html>
<html lang="en">
<head>
<meta charset="utf-8">
<title>Brickline Gains – Home Renovation</title>
<link rel="stylesheet" href="https://fonts.googleapis.com/css2?family=Cinzel:wght@400;700&family=Open+Sans:wght@400;600;700&display=swap">
<style>
:root{
  --orange:#f0841c;
  --navy:#0f2a5e;
  --navy-deep:#0b1f47;
  --ink:#2b2b2b;
  --muted:#6d6d6d;
  --beige:#f7f1ea;
  --grey:#ececec;
  --line:#dcdcdc;
  --white:#fff;
}
*{box-sizing:border-box;margin:0;padding:0}
html,body{width:1200px;height:3820px;overflow:hidden}
body{font-family:"Open Sans",Arial,sans-serif;color:var(--ink);background:var(--white);font-size:15px;line-height:1.6}
.heading{font-family:"Cinzel",Georgia,serif;font-weight:700;text-transform:uppercase;letter-spacing:2px;color:var(--navy)}
.heading em{font-style:normal;color:var(--orange)}
.btn{display:inline-block;font-weight:700;font-size:13px;letter-spacing:1px;text-transform:uppercase;padding:12px 26px;border-radius:3px;color:var(--white);white-space:nowrap}
.btn-orange{background:var(--orange)}
.btn-navy{background:var(--navy)}
.section-mark{display:block;width:40px;height:4px;background:var(--orange);margin:0 auto 14px}

/* header */
.site-header{position:absolute;top:0;left:0;width:1200px;height:80px;background:var(--white);display:flex;align-items:center;padding:0 60px;z-index:2}
.brand{display:flex;align-items:center;gap:10px;font-weight:700;font-size:20px;color:var(--navy)}
.brand-square{width:22px;height:22px;background:var(--orange)}
.main-nav{display:flex;gap:30px;margin-left:120px;font-size:13px;font-weight:600;color:var(--ink)}
.main-nav .active{color:var(--orange)}
.header-phone{margin-left:auto;font-size:14px;font-weight:600;color:var(--navy);margin-right:26px}

/* hero */
.hero{position:absolute;top:80px;left:0;width:1200px;height:568px;background:linear-gradient(180deg,#2e3d55 0%,#5b5e66 45%,#6b5442 80%,#3e3126 100%);color:var(--white);text-align:center}
.hero-title{font-family:"Cinzel",Georgia,serif;font-size:64px;letter-spacing:6px;margin-top:170px;font-weight:400}
.hero-tag{font-size:20px;letter-spacing:4px;margin-top:8px}
.hero .btn{margin-top:36px}

/* who we are */
.who{position:absolute;top:648px;left:0;width:1200px;height:352px;text-align:center;padding-top:70px}
.who .heading{font-size:40px}
.who p{width:720px;margin:22px auto 0;font-size:14px;color:var(--muted)}
.who p + p{margin-top:10px}
.who em{font-style:normal;color:var(--orange)}

/* projects */
.projects{position:absolute;top:1000px;left:0;width:1200px;height:560px;background:var(--beige);text-align:center;padding-top:56px}
.projects .heading{font-size:40px}
.project-row{display:flex;gap:40px;justify-content:center;margin-top:40px}
.project-card{width:312px;height:310px;position:relative}
.project-overlay{position:absolute;inset:0;background:rgba(15,42,94,.55);color:var(--white);padding:40px 36px;text-align:center}
.project-overlay h3{font-family:"Cinzel",Georgia,serif;font-size:20px;font-weight:400;line-height:1.3}
.project-overlay p{font-size:12px;margin-top:12px}
.project-overlay .btn{margin-top:24px}
.slide-arrow{position:absolute;width:32px;height:32px;border-radius:50%;background:#c9c9c9;display:flex;align-items:center;justify-content:center}

/* event */
.event{position:absolute;top:1580px;left:0;width:1200px;height:500px;padding:60px 60px 0}
.event .heading{font-size:36px;margin-top:10px}
.event-text{width:470px}
.event-text .mark{width:40px;height:4px;background:var(--orange)}
.event-text p{font-size:14px;color:var(--muted);margin:18px 0 26px}
.event-media{position:absolute;left:598px;top:90px;width:540px;height:346px}

/* ebook */
.ebook{position:absolute;top:2100px;left:0;width:1200px;height:470px;background:var(--grey)}
.ebook-media{position:absolute;left:90px;top:40px;width:440px;height:380px}
.ebook-text{position:absolute;left:620px;top:90px;width:420px}
.ebook-text .mark{width:40px;height:4px;background:var(--orange)}
.ebook .heading{font-size:32px;color:var(--orange);margin-top:10px}
.ebook-text p{font-size:14px;color:var(--muted);margin:16px 0 26px}

/* blog */
.blog{position:absolute;top:2590px;left:0;width:1200px;height:370px;text-align:center;padding-top:44px}
.blog .heading{font-size:40px}
.blog-row{display:flex;gap:40px;justify-content:center;margin-top:38px;text-align:left}
.post{width:330px;display:flex;gap:14px}
.post-date{font-family:"Cinzel",Georgia,serif;font-weight:700;color:var(--orange);font-size:22px;line-height:1.2;text-align:center;border-right:1px solid var(--line);padding-right:12px}
.post h3{font-family:"Cinzel",Georgia,serif;font-size:17px;color:var(--navy);line-height:1.25}
.post p{font-size:13px;color:var(--muted);margin-top:8px}
.post p em{font-style:normal;color:var(--orange)}

/* testimonials */
.clients{position:absolute;top:2960px;left:0;width:1200px;height:440px;background:var(--grey);text-align:center;padding-top:30px}
.clients .heading{font-size:36px}
.client-row{display:flex;gap:52px;justify-content:center;margin-top:36px}
.client-card{width:312px;height:300px;background:var(--white);padding:26px 30px;text-align:center}
.avatar{width:64px;height:64px;border-radius:50%;background:linear-gradient(#c7b8a8,#8d7a68);margin:0 auto}
.client-card h4{font-size:14px;margin-top:10px;color:var(--navy)}
.client-card p{font-size:13px;color:var(--muted);margin-top:10px}
.client-card .more{display:block;font-size:12px;color:var(--navy);margin-top:14px;font-weight:600}

/* footer */
.site-footer{position:absolute;top:3400px;left:0;width:1200px;height:340px;display:flex;padding:50px 60px 0}
.footer-col{flex:1}
.footer-col + .footer-col{border-left:1px solid var(--line);padding-left:50px}
.footer-col h5{font-size:22px;font-weight:400;color:var(--navy);margin-bottom:16px}
.footer-col li{list-style:none;font-size:14px;color:var(--muted);line-height:1.9}
.contact-item{display:flex;align-items:center;gap:12px;font-size:14px;color:var(--muted);margin-bottom:16px}
.social{display:flex;gap:10px;justify-content:flex-end}
.social span{width:36px;height:36px;border-radius:50%}
.col-follow{text-align:right}
.copyright{position:absolute;top:3740px;left:0;width:1200px;height:80px;background:var(--navy-deep);color:#c9d1e0;font-size:13px;display:flex;align-items:center;justify-content:center}
</style>
</head>
<body>

<header class="site-header">
  <div class="brand"><span class="brand-square"></span>Brickline Gains</div>
  <nav class="main-nav">
    <span class="active">HOME</span><span>BLOG</span><span>EVENTS</span><span>TESTIMONIAL</span><span>CONTACT</span>
  </nav>
  <span class="header-phone">1300 - 482 - 615</span>
  <span class="btn btn-orange">Book My Seat Now</span>
</header>

<section class="hero" role="img" aria-label="Photo of a renovated two-storey family house at dusk with lit windows and a garage">
  <h1 class="hero-title">HOME RENOVATION</h1>
  <p class="hero-tag">PROGRESSIVE &nbsp;|&nbsp; PERSONAL &nbsp;|&nbsp; PROFESSIONAL</p>
  <span class="btn btn-orange">Book My Seat Now</span>
</section>

<section class="who">
  <span class="section-mark"></span>
  <h2 class="heading">Who <em>We Are</em></h2>
  <p>Hi I'm <em>Liam</em> from Brickline Gains, and my business partner, Owen and I have been investing in property for over <em>15 years</em>.</p>
  <p>During the past 4 years we have completed 20 renovation projects, and as a result of our successes, we have created a Proven Property Renovation Step-by-Step Blueprint that we use every time we renovate a property to reduce risks, minimise costs and maximise profits.</p>
</section>

<section class="projects">
  <span class="section-mark"></span>
  <h2 class="heading"><em>Our Project</em></h2>
  <div class="project-row">
    <div class="project-card" role="img" aria-label="Photo of a renovated house facade" style="background:linear-gradient(160deg,#8aa0b8,#5d6d60)">
      <div class="project-overlay">
        <h3>HOME<br>RENOVATION</h3>
        <p>Simple ideas that lift value, cut costs and add real appeal for buyers.</p>
        <span class="btn btn-orange">View More</span>
      </div>
    </div>
    <div class="project-card" role="img" aria-label="Photo of a red brick townhouse row with a green lawn" style="background:linear-gradient(180deg,#a9c3dd 0%,#9a4d38 45%,#7a3b2c 75%,#5d7a3a 100%)"></div>
    <div class="project-card" role="img" aria-label="Photo of a bright renovated bedroom with a pendant light" style="background:linear-gradient(180deg,#efe9e1 0%,#d8ccbd 55%,#8b7a6a 100%)"></div>
  </div>
  <span class="slide-arrow" style="left:18px;top:320px"><svg width="12" height="12" viewBox="0 0 12 12"><path d="M8 1 3 6l5 5" stroke="#fff" stroke-width="2" fill="none"/></svg></span>
  <span class="slide-arrow" style="right:18px;top:320px"><svg width="12" height="12" viewBox="0 0 12 12"><path d="M4 1l5 5-5 5" stroke="#fff" stroke-width="2" fill="none"/></svg></span>
</section>

<section class="event">
  <div class="event-text">
    <div class="mark"></div>
    <h2 class="heading">Awesome <em>Event</em></h2>
    <p>Join our two hour evening workshop and learn the exact steps we follow on every renovation project. We walk you through how to find the right property, set a realistic budget, choose trades you can trust and plan a timeline that keeps costs under control. You will see real numbers from our past projects, hear the mistakes we made early on and leave with a clear plan you can start using this week. Seats are limited, so bring your partner and questions.</p>
    <span class="btn btn-navy">Read More</span>
  </div>
  <div class="event-media" role="img" aria-label="Photo of an audience seated in a dark hall facing a lit presentation screen" style="background:linear-gradient(180deg,#3a4150 0%,#7c8796 35%,#5a5048 65%,#2a2420 100%)"></div>
</section>

<section class="ebook">
  <div class="ebook-media" role="img" aria-label="Illustration of three renovation eBook covers standing together" style="background:linear-gradient(135deg,#f3c9a0 0%,#7fb6dc 50%,#e9e2d6 100%)"></div>
  <div class="ebook-text">
    <div class="mark"></div>
    <h2 class="heading">Download Our Ebook</h2>
    <p>Get our free guide with ten practical tips for renovating for profit. It covers picking the right suburb, working out your numbers, managing trades and adding value where buyers notice it most. Written for busy families who want results.</p>
    <span class="btn btn-navy">Download Now</span>
  </div>
</section>

<section class="blog">
  <span class="section-mark"></span>
  <h2 class="heading"><em>Latest Blog</em></h2>
  <div class="blog-row">
    <article class="post">
      <div class="post-date">14<br>17</div>
      <div><h3>How I Moved From Full-Time Teaching</h3><p>Hi Everyone, I'm Liam for Brickline Gains, and I thought I'd give you a video case study of ... <em>[...]</em></p></div>
    </article>
    <article class="post">
      <div class="post-date">14<br>17</div>
      <div><h3>7 Tips To Reduce Risk When Renovating For Profit</h3><p>Hi Everyone, I'm Liam for Brickline Gains, and I thought I'd give you a video case study of ... <em>[...]</em></p></div>
    </article>
    <article class="post">
      <div class="post-date">14<br>17</div>
      <div><h3>How To Attain Financial Freedom Through</h3><p>Hi Everyone, I'm Liam for Brickline Gains, and I thought I'd give you a video case study of ... <em>[...]</em></p></div>
    </article>
  </div>
</section>

<section class="clients">
  <span class="section-mark"></span>
  <h2 class="heading">What Our <em>Client</em> Say</h2>
  <div class="client-row">
    <div class="client-card"><div class="avatar" role="img" aria-label="Client portrait photo"></div><h4>Rowan Pike</h4><p>The workshop gave us a clear plan and the confidence to start our first renovation. We finished on budget and sold for a strong profit within months.</p><span class="more">READ MORE</span></div>
    <div class="client-card"><div class="avatar" role="img" aria-label="Client portrait photo"></div><h4>Elise Brand</h4><p>As working parents we had little spare time. The step by step system kept everything simple, and the mentoring helped us avoid costly mistakes.</p><span class="more">READ MORE</span></div>
    <div class="client-card"><div class="avatar" role="img" aria-label="Client portrait photo"></div><h4>Mark</h4><p>Honest advice, real numbers and great support. We have now completed two projects and are planning the third with the team's guidance.</p><span class="more">READ MORE</span></div>
  </div>
  <span class="slide-arrow" style="left:18px;top:250px"><svg width="12" height="12" viewBox="0 0 12 12"><path d="M8 1 3 6l5 5" stroke="#fff" stroke-width="2" fill="none"/></svg></span>
  <span class="slide-arrow" style="right:18px;top:250px"><svg width="12" height="12" viewBox="0 0 12 12"><path d="M4 1l5 5-5 5" stroke="#fff" stroke-width="2" fill="none"/></svg></span>
</section>

<footer class="site-footer">
  <div class="footer-col">
    <h5>Quick Links</h5>
    <ul><li>Home</li><li>About</li><li>Blog</li><li>Testimonial</li><li>Event</li><li>Contact</li></ul>
  </div>
  <div class="footer-col">
    <h5>Contact Us</h5>
    <div class="contact-item"><svg width="16" height="18" viewBox="0 0 16 18"><path d="M8 1a6 6 0 0 0-6 6c0 4.5 6 10 6 10s6-5.5 6-10a6 6 0 0 0-6-6z" fill="var(--orange)"/><circle cx="8" cy="7" r="2.2" fill="#fff"/></svg>Level 4, Riverside Lane</div>
    <div class="contact-item"><svg width="16" height="16" viewBox="0 0 16 16"><path d="M3 1h3l1.5 4-2 1.5a9 9 0 0 0 4 4L11 8.5l4 1.5v3a2 2 0 0 1-2 2A13 13 0 0 1 1 3a2 2 0 0 1 2-2z" fill="var(--orange)"/></svg>1300 482 615</div>
    <div class="contact-item"><svg width="18" height="14" viewBox="0 0 18 14"><rect x="1" y="1" width="16" height="12" rx="1" fill="var(--orange)"/><path d="M1 2l8 6 8-6" stroke="#fff" stroke-width="1.4" fill="none"/></svg>admin@bricklinegains.com.au</div>
  </div>
  <div class="footer-col col-follow">
    <h5>Follow Us</h5>
    <div class="social"><span style="background:#3b5998"></span><span style="background:#2aa3ef"></span><span style="background:#dd4b39"></span></div>
  </div>
</footer>

<div class="copyright">Copyright 2015 - Brickline Gains Pty Ltd.</div>

</body>
</html>
```